Landing Page für Persönlichkeitsquiz
Zielgruppe
Persönlichkeitsquiz für Menschen über 40 Jahren die bessere Entscheidungen treffen möchten.
Aufgabenstellung
Landinpage Design plus QUIZ ( 6 Schritte)
Vollständige Projektbeschreibung:
Projektbeschreibung
„Roaming Sideways QUIZ“
roamingsideways.example
- Responsive Design für mobile & website (Most users: mobile)
- Design wird Grundlage für spätere Website
Dieses Quiz wendet sich an Menschen über 40 Jahre, die ihre persönlichen Lebensziele besser erreichen möchten. Bitte denke daran, dass Menschen in unserem Alter schon schlechter sehen – also bitte eine gut lesbare & etwas größere Schrift verwenden!
Auftrag:
QUIZ mit mehreren Runden
Schritte des Quiz:
1. Landingpage
1.1 Video (youtube eingebunden)
1.2 Text
1.3 „Start Quiz“ Button
1.4 „Bekannt aus“ mit Logos von Medien in denen Marv Olden besprochen wurde.
1.5 Testimonials?
QUIZ (Popup)
2. Erste Runde: „Kille“ alle Antworten die Dich nicht interessieren. Total 64 Antworten.
2.1 Text mit Aufgabenbeschreibung „Kille“ alle Antworten die Dich nicht interessieren. Du hast zwei Minuten.“
2.2 Ein Button pro Antwort (wie bei Lernivo)
2.3 Zwei Buttons pro Reihe
2.4 Oben: Progress bar
2.5 Oben: Countdown clock, Restzeit: 2 Minuten
3. Zweite Runde: „Wähle max. 18 Antworten aus die überleben sollen.“
3.1 Text mit Aufgabenbeschreibung „Wähle max. 18 Antworten aus die überleben sollen.“
3.2 Ein Button pro Antwort (wie bei Lernivo)
3.3 Zwei Buttons pro Reihe
3.4 Oben: Progress bar
3.5 Oben: Countdown clock, Restzeit: 60 Sekunden
3.6 Zähler der noch verfügbaren Antworten. Hier: Noch 18, noch 17, noch 16.. etc.
4. Dritte Runde: „Nur 9 Antworten dürfen überleben. Go!“
4.1 Text mit „Nur 9 Antworten dürfen überleben. Go!“
4.2 Ein Button pro Antwort (wie bei Lernivo)
4.3 Zwei Buttons pro Reihe
4.4 Oben: Progress bar
4.5 Oben: Countdown clock, Restzeit 45 ..

```html
<!DOCTYPE html>
<html lang="de">
<head>
<meta charset="utf-8">
<title>Roaming Sideways Quiz</title>
<link href="https://fonts.googleapis.com/css2?family=Open+Sans:wght@400;600;700&display=swap" rel="stylesheet">
<style>
:root{
  --hero-a:#4a1a9e;
  --hero-b:#2e109e;
  --band:#643bb9;
  --band-alt:#5b35ad;
  --footer:#3a169c;
  --ink-dark:#24104a;
  --ink-dim:#6a3fc4;
  --accent:#c06ad6;
  --gold:#e0a830;
  --btn:#6a2d68;
  --btn-text:#9c5cdc;
  --card:#6a40c0;
  --card-edge:#5226b0;
  --grey:#6a6a6a;
  --white:#fff;
}
*{box-sizing:border-box;margin:0;padding:0}
html,body{width:864px;height:1200px;overflow:hidden}
body{font-family:"Open Sans",sans-serif;position:relative;background:var(--band);color:var(--ink-dark)}
.abs{position:absolute}
.hero{left:0;top:0;width:864px;height:409px;background:linear-gradient(120deg,var(--hero-a),var(--hero-b))}
.brand{left:63px;top:40px;font-size:12.5px;font-weight:700;line-height:17px;color:var(--ink-dim);letter-spacing:.2px}
.lang{left:718px;top:58px;width:16px;height:16px;border-radius:50%;background:linear-gradient(#1a0a2a 33%,#9a1a3a 33% 66%,#b08a20 66%)}
.lang-chev{left:740px;top:61px}
.nav{left:771px;top:58px;font-size:10px;color:var(--ink-dim)}
.hero-title{left:63px;top:142px;font-size:18.5px;font-weight:700;line-height:25px;color:var(--ink-dim)}
.hero-text{left:63px;top:205px;font-size:9.5px;line-height:12.5px;color:var(--ink-dim);width:300px}
.btn{display:flex;align-items:center;justify-content:center;gap:5px;background:var(--btn);color:var(--btn-text);font-weight:700;font-size:10px;border-radius:14px;height:27px;width:94px}
.hero-btn{left:63px;top:260px}
.hero-media{left:725px;top:107px;width:75px;height:201px;background:#6f2fb0}
.hero-dot{left:727px;top:86px;width:30px;height:30px;border-radius:50%;background:#4a1db0}
.hero-clip{left:740px;top:160px}

.modal{left:125px;top:83px;width:614px;height:310px;background:var(--white);border-bottom:4px solid var(--accent);box-shadow:0 2px 10px rgba(0,0,0,.15);z-index:2}
.step{left:419px;top:70px;width:26px;height:26px;border-radius:50%;background:var(--accent);border:2px solid var(--white);color:var(--white);font-weight:700;font-size:12px;display:flex;align-items:center;justify-content:center;z-index:3}
.back{left:23px;top:17px;display:flex;align-items:center;gap:5px;color:var(--gold);font-size:10px;font-weight:700}
.timer{left:222px;top:17px;display:flex;align-items:center;gap:5px;font-size:10.5px}
.timer b{color:var(--accent)}
.timer span{color:var(--grey);border-left:1px solid #ccc;padding-left:4px}
.done{right:23px;top:17px;font-size:9.5px;font-weight:700;color:var(--accent)}
.progress{left:23px;top:43px;width:568px;height:8px;border-radius:4px;background:var(--accent)}
.q-title{left:0;width:614px;top:68px;text-align:center;font-size:16px;font-weight:700;color:var(--grey)}
.q-sub{left:0;width:614px;top:89px;text-align:center;font-size:11px;color:var(--grey)}
.answer{left:124px;width:179px;height:35px;background:var(--accent);color:var(--white);font-size:9.5px;display:flex;align-items:center;padding-left:7px}
.slot{left:310px;width:179px;height:35px;border:1px dashed #bbb;color:#bbb;font-weight:700;font-size:16px;display:flex;align-items:center;justify-content:center}
.nearly{left:19px;top:255px;font-size:8.5px;line-height:12px;color:var(--grey)}
.nearly b{color:var(--accent)}
.result{right:23px;top:268px;display:flex;align-items:center;gap:5px;color:var(--gold);font-size:10px;font-weight:700}

.section-title{left:0;width:864px;text-align:center;font-size:11px;font-weight:700;color:var(--ink-dark)}
.rule{left:417px;width:30px;height:2px;background:var(--accent)}
.press{left:0;top:409px;width:864px;height:208px;background:var(--band)}
.press-arrow{width:14px;height:14px;border-radius:50%;background:var(--btn);top:510px;display:flex;align-items:center;justify-content:center}
.press-row{left:90px;top:497px;width:690px;height:40px;display:flex;align-items:center;justify-content:space-between}
.press-name{font-size:12px;font-weight:700;color:#140a22;display:flex;align-items:center;gap:4px;white-space:nowrap}
.press-name i{display:block;width:10px;height:10px;background:#140a22}
.deco-right{left:832px;top:430px;width:120px;height:125px;border-radius:50%;background:#3a14a0}

.voices{left:0;top:617px;width:864px;height:261px;background:var(--band-alt)}
.deco-left{left:-85px;top:655px;width:120px;height:130px;border-radius:50%;background:#4a1aa8}
.card{top:698px;width:241px;height:112px;background:var(--card);border-bottom:3px solid var(--card-edge)}
.avatar{left:12px;top:13px;width:49px;height:49px;border-radius:50%;background:linear-gradient(135deg,#5a3a6a,#3a2040)}
.who{left:74px;top:24px}
.who strong{display:block;font-size:10px;font-weight:700;color:var(--ink-dark)}
.who small{display:block;font-size:7px;color:var(--ink-dark);margin-top:3px}
.who small b{font-weight:700}
.bubble{right:10px;top:9px}
.quote{left:12px;top:70px;width:222px;font-size:8px;line-height:11px;color:var(--ink-dark)}

.about{left:0;top:878px;width:864px;height:286px;background:var(--band)}
.portrait{left:112px;top:951px;width:148px;height:148px;border-radius:50%;background:linear-gradient(160deg,#7a5aa8,#4a2a7a)}
.deco-small{left:78px;top:1074px;width:40px;height:40px;border-radius:50%;background:#3a16a4}
.about-head{left:312px;top:951px;font-size:11.5px;font-weight:700;color:var(--ink-dark)}
.about-text{left:312px;width:480px;font-size:8px;line-height:11px;color:var(--ink-dark)}

.footer{left:0;top:1164px;width:864px;height:36px;background:linear-gradient(90deg,#4a1a9e,var(--footer));font-size:8.5px;color:#5a3ad0}
.footer span{position:absolute;top:11px}
</style>
</head>
<body>
<div class="abs hero"></div>
<div class="abs brand">ROAMING<br>SIDEWAYS</div>
<div class="abs lang"></div>
<svg class="abs lang-chev" width="10" height="8" viewBox="0 0 10 8"><path d="M1 2l4 4 4-4" fill="none" stroke="#6a3fc4" stroke-width="1.3"/></svg>
<div class="abs nav">Fragen</div>
<div class="abs hero-title">Herzlich willkommen<br>bei Roaming Sideways</div>
<div class="abs hero-text">Lorem ipsum dolor sit amet, consetetur sed diam nonumy eirmod tempor invidunt ut labore aliquyam erat, sed diam voluptua.</div>
<div class="abs btn hero-btn"><svg width="9" height="9" viewBox="0 0 10 10"><path d="M1 5h7M5 2l3 3-3 3" fill="none" stroke="#9c5cdc" stroke-width="1.5"/></svg>Quiz starten</div>
<div class="abs hero-dot"></div>
<div class="abs hero-media" role="img" aria-label="Platz für eingebundenes Einführungsvideo"></div>
<svg class="abs hero-clip" width="18" height="18" viewBox="0 0 18 18"><rect x="2" y="6" width="14" height="6" rx="3" transform="rotate(-40 9 9)" fill="none" stroke="#1a0a2a" stroke-width="1.6"/></svg>

<div class="abs step">5</div>
<div class="abs modal">
  <div class="abs back"><svg width="13" height="13" viewBox="0 0 14 14"><circle cx="7" cy="7" r="7" fill="#e0a830"/><path d="M8.5 4L5.5 7l3 3" fill="none" stroke="#fff" stroke-width="1.6"/></svg>zurück</div>
  <div class="abs timer"><svg width="13" height="13" viewBox="0 0 14 14"><circle cx="7" cy="7" r="6" fill="none" stroke="#c06ad6" stroke-width="1.4"/><path d="M7 3.5V7l2.5 1.5" fill="none" stroke="#c06ad6" stroke-width="1.4"/></svg><b>00 : 10</b><span>Restzeit: 10 Sekunden</span></div>
  <div class="abs done">100 % komplett</div>
  <div class="abs progress"></div>
  <div class="abs q-title">Sortiere die Antworten nach Relevanz.</div>
  <div class="abs q-sub">1= Am wichtigsten, 3= Am unwichtigsten</div>
  <div class="abs answer" style="top:121px">Lorem ipsum dela martime de.</div>
  <div class="abs slot" style="top:121px">1</div>
  <div class="abs answer" style="top:163px">Lorem ipsum dela martime de ma di.</div>
  <div class="abs slot" style="top:163px">2</div>
  <div class="abs answer" style="top:205px">Lorem ipsum dela martime de.</div>
  <div class="abs slot" style="top:205px">3</div>
  <div class="abs nearly">Du hast es<br><b>fast geschafft!</b></div>
  <div class="abs result">Resultat<svg width="13" height="13" viewBox="0 0 14 14"><circle cx="7" cy="7" r="7" fill="#e0a830"/><path d="M5.5 4l3 3-3 3" fill="none" stroke="#fff" stroke-width="1.6"/></svg></div>
</div>

<div class="abs press"></div>
<div class="abs deco-right"></div>
<div class="abs section-title" style="top:437px">Bekannt aus</div>
<div class="abs rule" style="top:458px"></div>
<div class="abs press-arrow" style="left:62px"><svg width="6" height="8" viewBox="0 0 6 8"><path d="M4.5 1L1.5 4l3 3" fill="none" stroke="#3a1a4a" stroke-width="1.3"/></svg></div>
<div class="abs press-row">
  <span class="press-name"><i></i>Tagblick</span>
  <span class="press-name">Abendpost</span>
  <span class="press-name">Nordwelle</span>
  <span class="press-name">weltecho</span>
  <span class="press-name">Radio Zwei</span>
  <span class="press-name">Kanal West</span>
  <span class="press-name"><i></i>Infokanal</span>
</div>
<div class="abs press-arrow" style="left:787px"><svg width="6" height="8" viewBox="0 0 6 8"><path d="M1.5 1l3 3-3 3" fill="none" stroke="#3a1a4a" stroke-width="1.3"/></svg></div>
<div class="abs btn" style="left:385px;top:560px"><svg width="9" height="9" viewBox="0 0 10 10"><path d="M1 5h7M5 2l3 3-3 3" fill="none" stroke="#9c5cdc" stroke-width="1.5"/></svg>Quiz starten</div>

<div class="abs voices"></div>
<div class="abs deco-left"></div>
<div class="abs section-title" style="top:651px">Was sagen andere zum Quiz</div>
<div class="abs rule" style="top:672px"></div>

<div class="abs card" style="left:63px">
  <div class="abs avatar" role="img" aria-label="Porträtfoto von Fatima Mustermann"></div>
  <div class="abs who"><strong>Fatima Mustermann</strong><small>aus&nbsp; <b>Berlin</b></small></div>
  <svg class="abs bubble" width="14" height="14" viewBox="0 0 14 14"><path d="M7 1.5a5.5 5 0 1 1-2.8 9.3L1.5 12.5l.9-3A5.5 5 0 0 1 7 1.5z" fill="none" stroke="#3a18a0" stroke-width="1.2"/></svg>
  <p class="abs quote">Lorem ipsum dolor sit amet, consetetur sadipscing elitr, sed diam nonumy eirmod tempor invidunt ut labore et dolore magna aliquyam erat, sed diam voluptua.</p>
</div>
<div class="abs card" style="left:312px">
  <div class="abs avatar" role="img" aria-label="Porträtfoto von James Mustermelian"></div>
  <div class="abs who"><strong>James Mustermelian</strong><small>aus&nbsp; <b>Bayern</b></small></div>
  <svg class="abs bubble" width="14" height="14" viewBox="0 0 14 14"><path d="M7 1.5a5.5 5 0 1 1-2.8 9.3L1.5 12.5l.9-3A5.5 5 0 0 1 7 1.5z" fill="none" stroke="#3a18a0" stroke-width="1.2"/></svg>
  <p class="abs quote">Lorem ipsum dolor sit amet, consetetur sadipscing elitr, sed diam nonumy eirmod tempor invidunt ut labore et dolore magna aliquyam erat, sed diam voluptua.</p>
</div>
<div class="abs card" style="left:560px">
  <div class="abs avatar" role="img" aria-label="Porträtfoto von Christiane Weißfuss"></div>
  <div class="abs who"><strong>Christiane Weißfuss</strong><small>aus&nbsp; <b>Hannover</b></small></div>
  <svg class="abs bubble" width="14" height="14" viewBox="0 0 14 14"><path d="M7 1.5a5.5 5 0 1 1-2.8 9.3L1.5 12.5l.9-3A5.5 5 0 0 1 7 1.5z" fill="none" stroke="#3a18a0" stroke-width="1.2"/></svg>
  <p class="abs quote">Lorem ipsum dolor sit amet, consetetur sadipscing elitr, sed diam nonumy eirmod tempor invidunt ut labore et dolore magna aliquyam erat, sed diam voluptua.</p>
</div>
<div class="abs btn" style="left:385px;top:833px"><svg width="9" height="9" viewBox="0 0 10 10"><path d="M1 5h7M5 2l3 3-3 3" fill="none" stroke="#9c5cdc" stroke-width="1.5"/></svg>Quiz starten</div>

<div class="abs about"></div>
<div class="abs section-title" style="top:902px">Über MarvOlden</div>
<div class="abs rule" style="top:922px"></div>
<div class="abs portrait" role="img" aria-label="Foto von Marv Olden mit Partnerin"></div>
<div class="abs deco-small"></div>
<div class="abs about-head">Was meine Oma mich lehrte</div>
<p class="abs about-text" style="top:984px">Die einflussreichste Person in meinem Leben war meine Großmutter. Sie wurde im Deutschen Kaiserreich geboren; erlebte zwei Weltkriege, die Mondlandung und Fenstersoft 95.</p>
<p class="abs about-text" style="top:1016px">Während des Krieges ging sie nach Dresden, um ihre Tochter aus der “Landverschickung” nach Hause zu holen, und zwang die Schulleiterin, ihre Tochter zurückzugeben. Dann brachte Oma sie (die Tochter, nicht die Schulleiterin) durch halb Deutschland und das ganze Chaos des zerstörten Eisenbahnnetzes nach Hause. Dresden wurde in der nächsten Nacht bombardiert, meine Mutter hätte das nicht überlebt.</p>
<p class="abs about-text" style="top:1071px">Meine Großmutter lehrte mich, Menschen nach ihren Taten zu beurteilen, nicht nach ihren Worten.</p>
<div class="abs btn" style="left:312px;top:1095px"><svg width="9" height="9" viewBox="0 0 10 10"><path d="M1 5h7M5 2l3 3-3 3" fill="none" stroke="#9c5cdc" stroke-width="1.5"/></svg>Quiz starten</div>

<footer class="abs footer">
  <span style="left:63px">© Roaming Sideways QUIZ</span>
  <span style="left:634px">Impressum</span>
  <span style="left:700px">Datenschutz</span>
  <span style="left:767px">Sitemap</span>
</footer>
</body>
</html>
```